Create a Magazine Ad for an asbestos law firm

we need an 8 X 13 ad to be on the back of a magazine cover. We have the text Attached and want a similar look and feel to our website : www.claimsharbor-help.com. The ad should be targeted to white males 55 years or older who are conservative and worked in industry or industrial plants. The main offer is a free case review and trying to get them to call the telephone number.

Target Market(s)

White collar men who worked in industrial plants. Age 55 years or older.

Industry/Entity Type

Legal

Requirements
Must have
• Pictures of white middle class conservative man or man and woman
Nice to have
• look at www.claimsharbor-help.com to an. idea of what we are looking for

```html
<!DOCTYPE html>
<html lang="en">
<head>
<meta charset="utf-8">
<title>Mesothelioma &amp; Asbestos Compensation</title>
<link href="https://fonts.googleapis.com/css2?family=Montserrat:wght@600;700;800&family=Poppins:wght@400;500;600;700;800&display=swap" rel="stylesheet">
<style>
  :root{
    --navy:#0c1a4a;
    --navy-deep:#07113a;
    --ink:#0b1240;
    --gold:#f3d000;
    --cream:#faf5df;
    --gray:#555a66;
    --white:#ffffff;
  }
  *{margin:0;padding:0;box-sizing:border-box}
  html,body{width:738px;height:1200px;overflow:hidden;background:var(--white)}
  .ad{position:relative;width:738px;height:1200px;overflow:hidden;font-family:"Poppins",sans-serif;color:var(--ink)}
  .abs{position:absolute}

  .hero{left:0;top:0;width:738px;height:336px;
    background:linear-gradient(180deg,#1b2f6e 0%,#2a4484 45%,#34508c 75%,#4a5a7c 100%)}
  .hero-title{left:36px;top:34px;font-family:"Montserrat",sans-serif;font-weight:600;font-size:43px;line-height:55px;color:var(--white);letter-spacing:-0.3px;white-space:nowrap}
  .hero-sub{left:36px;top:155px;font-size:20.4px;color:var(--white);white-space:nowrap}
  .exposure{left:36px;font-size:16.9px;color:var(--white);white-space:nowrap}
  .exposure span{margin-right:14px}
  .exposure span::before{content:"•";margin-right:12px}
  .gold-band{left:0;top:336px;width:738px;height:16px;background:var(--gold)}

  .cream{background:var(--cream)}
  .h2{font-family:"Montserrat",sans-serif;font-weight:800;font-size:23.5px;color:var(--ink);white-space:nowrap}
  .bullets{list-style:none;left:48px}
  .bullets li{font-size:15.4px;color:var(--gray);position:relative;padding-left:24px;white-space:nowrap}
  .bullets li::before{content:"";position:absolute;left:0;top:50%;width:5px;height:5px;margin-top:-3px;border-radius:50%;background:var(--gray)}

  .vet-text{left:43px;top:673px;width:386px;font-size:15px;line-height:18.5px;letter-spacing:-0.1px;color:var(--gray);text-align:justify}
  .photo-frame{left:475px;top:635px;width:219px;height:140px;background:var(--navy-deep)}
  .photo{left:466px;top:642px;width:221px;height:146px;
    background:linear-gradient(180deg,#c9d6e2 0%,#9fb2c4 45%,#3c4a52 60%,#e8edf2 100%)}

  .sub{left:46px;top:832px;font-family:"Montserrat",sans-serif;font-weight:700;font-size:15px;color:var(--ink)}
  .table{left:43px;top:870px;width:652px;height:167px;border:2px solid var(--ink);display:grid;
    grid-template-columns:213px 212px 1fr;grid-template-rows:84px 1fr}
  .cell{border-right:2px solid var(--ink);border-bottom:2px solid var(--ink);text-align:center;padding-top:14px}
  .cell:nth-child(3n){border-right:none}
  .cell:nth-child(n+4){border-bottom:none;padding-top:6px}
  .amount{font-weight:700;font-size:21px;line-height:26px;color:var(--ink)}
  .label{font-size:15.6px;line-height:18.5px;color:var(--gray);margin-top:4px;white-space:nowrap}

  .footer{left:0;top:1050px;width:738px;height:150px;
    background:linear-gradient(180deg,#142a7a 0%,#0b1a55 55%,#0d1d45 100%)}
  .footer-line{left:44px;top:1062px;width:660px;font-size:15.4px;line-height:19px;color:var(--white);font-weight:500}
  .footer-line strong{color:var(--gold);font-weight:800}
  .call{left:0;top:1103px;width:738px;text-align:center;font-weight:800;font-size:30.5px;color:var(--white);white-space:nowrap}
  .call .num{color:var(--gold);margin-left:4px}
  .call svg{vertical-align:-3px;margin-right:12px}
  .rule{left:167px;top:1152px;width:233px;height:1.5px;background:var(--white)}
  .free{left:415px;top:1141px;font-weight:700;font-size:17px;color:var(--white)}
  .sponsor{left:44px;top:1168px;font-size:15.4px;color:var(--white);font-weight:500}
  .sponsor strong{color:var(--gold);font-weight:800}
</style>
</head>
<body>
<div class="ad">
  <div class="abs hero" role="img" aria-label="Industrial refinery plant with towers and smokestacks under a blue sky"></div>
  <h1 class="abs hero-title">MESOTHELIOMA &amp;<br>ASBESTOS COMPENSATION</h1>
  <p class="abs hero-sub">COMMON ASBESTOS EXPOSURE THAT CAUSES MESOTHELIOMA</p>
  <p class="abs exposure" style="top:200px"><span>CONSTRUCTION</span><span>SHIPYARD</span><span>AUTOMOTIVE</span><span>INDUSTRIAL</span><span>PLUMBERS</span></p>
  <p class="abs exposure" style="top:230px;letter-spacing:-0.4px"><span style="margin-right:11px">PIPEFITTERS</span><span style="margin-right:11px">MINERS</span><span style="margin-right:11px">INSULATORS</span><span style="margin-right:11px">RAILROAD</span><span style="margin-right:11px">NAVY</span><span>POWER PLANTS</span></p>
  <p class="abs exposure" style="top:257px"><span>TEXTILE</span><span>SECOND HAND EXPOSURE FROM SPOUSE</span><span>WASHING CLOTHES</span></p>
  <p class="abs exposure" style="top:287px"><span>K&amp;M TALCUM POWDER / BABY POWDER</span></p>
  <div class="abs gold-band"></div>

  <h2 class="abs h2" style="left:44px;top:363px">CALL 1 800 555-0142 FOR A FREE CONSULTATION</h2>
  <ul class="abs bullets" style="top:401px;line-height:28px">
    <li>CALCULATE HOW MUCH YOU MAY BE OWED</li>
    <li>FILE YOUR MESOTHELIOMA CLAIM TODAY</li>
    <li>REPRESENTATIVES AVAILABLE 24/7</li>
  </ul>

  <div class="abs cream" style="left:0;top:491px;width:738px;height:126px"></div>
  <h2 class="abs h2" style="left:44px;top:498px">NATIONWIDE ASSISTANCE</h2>
  <ul class="abs bullets" style="top:533px;line-height:25px">
    <li>OVER $2 BILLION RECOVERED</li>
    <li>25 + YEAR OF LEGAL EXPERIENCE</li>
    <li>ATTORNEYS EXPEDITE QUICK PAYMENTS</li>
  </ul>

  <h2 class="abs h2" style="left:42px;top:638px">HELP WITH VETERAN BENEFITS</h2>
  <p class="abs vet-text">Depending on where you were exposed and a few other factors, you can get a settlement from 6 to 7 figures. Here are a few examples of Mesotheliom Settlements received by our clients. These figures are the total compensation after all attorney fees and expenses are deducted.</p>
  <div class="abs photo-frame"></div>
  <div class="abs photo" role="img" aria-label="Two navy sailors in white uniforms saluting by the sea, seen from behind"></div>

  <h2 class="abs h2" style="left:44px;top:803px">MESOTHELIOMA CLIENT RECOVERIES</h2>
  <p class="abs sub">after Attorneys Fees &amp; Expenses:</p>

  <div class="abs cream" style="left:0;top:860px;width:738px;height:190px"></div>
  <div class="abs table">
    <div class="cell"><div class="amount">$4,750,000</div><div class="label">NAVY EXPOSURE</div></div>
    <div class="cell"><div class="amount">$3,310,650</div><div class="label">HVAC EXPOSURE</div></div>
    <div class="cell"><div class="amount">$ 3,185,280</div><div class="label">PAPER MILL / CARPENTRY</div></div>
    <div class="cell"><div class="amount">$2,715,915</div><div class="label">MECHANICS<br>EXPOSURE</div></div>
    <div class="cell"><div class="amount">$1,886,58</div><div class="label">WIFE EXPOSED WASHING<br>HUSBANDS’ CLOTHING</div></div>
    <div class="cell"><div class="amount">$1,178,100</div><div class="label">K&amp;M TALC BABY<br>POWDER</div></div>
  </div>

  <div class="abs footer" role="img" aria-label="Industrial plant lit up at night"></div>
  <p class="abs footer-line"><strong>No Legal Fees unless You Win!</strong> We Get You Fair And Just Compensation From the Negligent Asbestos Product Manufacturers.</p>
  <p class="abs call"><svg width="22" height="22" viewBox="0 0 24 24" fill="none" stroke="#fff" stroke-width="2" stroke-linejoin="round"><path d="M5 3h4l2 5-2.5 1.5a11 11 0 0 0 6 6L16 13l5 2v4a2 2 0 0 1-2 2A16 16 0 0 1 3 5a2 2 0 0 1 2-2z"/><path d="M15 3a6 6 0 0 1 6 6M15 7a2 2 0 0 1 2 2"/></svg>Call Now <span class="num">1 800 555-0142</span></p>
  <div class="abs rule"></div>
  <p class="abs free">Free Consultation</p>
  <p class="abs sponsor"><strong>Sponsor :</strong> Harlan Brooks, Attorneys, Beaumont, TX</p>
</div>
</body>
</html>
```